BKA

Please send us some options for letterhead I attached our Logo. In addition to the Logo we need this information somewhere on the page

47 Fenbury Lane
Millbrook, CT 06455
203-481-7629

```html
<!DOCTYPE html>
<html lang="en">
<head>
<meta charset="utf-8">
<title>BKA Letterhead</title>
<link rel="stylesheet" href="https://fonts.googleapis.com/css2?family=Open+Sans:wght@400;600;700&display=swap">
<style>
  :root {
    --backdrop: #eef0f3;
    --paper: #ffffff;
    --brand-blue: #0a6fba;
    --brand-dark: #4a403c;
    --text-grey: #555555;
  }
  * { margin: 0; padding: 0; box-sizing: border-box; }
  html, body {
    width: 1200px;
    height: 1200px;
    overflow: hidden;
    background: var(--backdrop);
    font-family: "Open Sans", Arial, sans-serif;
  }
  .letterhead {
    position: absolute;
    left: 168px;
    top: 26px;
    width: 864px;
    height: 1150px;
    background: var(--paper);
    overflow: hidden;
  }
  .brand {
    position: absolute;
    top: 82px;
    left: 0;
    width: 100%;
    display: flex;
    justify-content: center;
    align-items: center;
    gap: 14px;
  }
  .brand-square {
    width: 46px;
    height: 46px;
    background: var(--brand-blue);
  }
  .brand-name {
    font-size: 46px;
    font-weight: 700;
    color: var(--brand-dark);
    letter-spacing: 2px;
    line-height: 1;
  }
  .corner-shapes {
    position: absolute;
    left: 0;
    bottom: 0;
    width: 864px;
    height: 240px;
  }
  .corner-shapes polygon { fill: var(--brand-blue); }
  .contact {
    position: absolute;
    top: 1084px;
    left: 0;
    width: 100%;
    display: flex;
    justify-content: center;
  }
  .contact-list {
    display: grid;
    grid-template-columns: auto auto;
    column-gap: 8px;
    row-gap: 0;
    font-size: 14px;
    line-height: 19px;
  }
  .contact-label {
    text-align: right;
    font-weight: 700;
    color: var(--brand-blue);
  }
  .contact-value { color: var(--text-grey); }
</style>
</head>
<body>
  <main class="letterhead">
    <header class="brand">
      <span class="brand-square"></span>
      <span class="brand-name">BKA</span>
    </header>

    <svg class="corner-shapes" viewBox="0 0 864 240" aria-hidden="true">
      <polygon points="0,0 0,240 238,240"/>
      <polygon points="864,0 864,240 626,240"/>
    </svg>

    <footer class="contact">
      <dl class="contact-list">
        <dt class="contact-label">Address:</dt>
        <dd class="contact-value">47 Fenbury Lane, Millbrook, CT&nbsp; 06455</dd>
        <dt class="contact-label">Phone:</dt>
        <dd class="contact-value">203-481-7629</dd>
      </dl>
    </footer>
  </main>
</body>
</html>
```